"Sun On Water" Gospel Presentation Booklet

I need a design for a 12 page (including front/back cover) square booklet, with religious images and aesthetically pleasing fonts/designs. I want it to be very simple, and very straightforward. The main focus of the project is it's content. So the design should be very nice, but also should point to the content, not take away from it, or create distraction. People should be more focused on the words than the imagery.

I enjoy modern designs, I need a sharp aesthetic that is clean and neat. Nothing over the top.
I have attached a word document with the content I would like on the pages.

Colors
0592cd
0255a3
33a6d7
85cae6
85acd3
3276b5
9bcb3b
f04a50
f68d4c

Requirements
Should not have
• Super feminine colors/aesthetics

```html
<!DOCTYPE html>
<html lang="en">
<head>
<meta charset="utf-8">
<title>Sun On Water – Gospel Booklet Spreads</title>
<link rel="stylesheet" href="https://fonts.googleapis.com/css2?family=Oswald:wght@400;500;700&display=swap">
<style>
  :root {
    --green: #9bcb3b;
    --sky: #85cae6;
    --red: #f04a50;
    --orange: #f68d4c;
    --navy: #0255a3;
    --steel: #85acd3;
    --white: #ffffff;
    --page: 588px;
    --gap-x: 24px;
    --gap-y: 25.6px;
  }
  * { box-sizing: border-box; margin: 0; padding: 0; }
  html, body {
    width: 1200px;
    height: 3656px;
    overflow: hidden;
    background: var(--white);
    font-family: "Oswald", "Arial Narrow", sans-serif;
    color: var(--white);
  }
  .booklet {
    display: grid;
    grid-template-columns: repeat(2, var(--page));
    grid-auto-rows: var(--page);
    column-gap: var(--gap-x);
    row-gap: var(--gap-y);
  }
  .page {
    position: relative;
    width: var(--page);
    height: var(--page);
  }
  .page::after {
    content: "";
    position: absolute;
    inset: 22px;
    border: 7px solid var(--white);
    pointer-events: none;
  }
  .page--green { background: var(--green); }
  .page--sky { background: var(--sky); }
  .page--red { background: var(--red); }
  .page--orange { background: var(--orange); }
  .page--navy { background: var(--navy); }
  .page--steel { background: var(--steel); }

  .title-page {
    display: flex;
    align-items: center;
    justify-content: center;
    text-align: center;
  }
  .section-title {
    font-weight: 700;
    font-size: 150px;
    line-height: 1;
    text-transform: uppercase;
    letter-spacing: -1px;
  }
  .section-title--small { font-size: 104px; }
  .cover-title {
    font-weight: 700;
    font-size: 118px;
    line-height: 1.02;
    text-transform: uppercase;
  }

  .text-page {
    display: flex;
    align-items: center;
    justify-content: center;
    text-align: center;
    padding: 60px 56px;
  }
  .body-copy {
    font-weight: 400;
    line-height: 1.62;
  }
  .body-copy--lg { font-size: 40px; }
  .body-copy--md { font-size: 36px; line-height: 1.5; }
  .body-copy--sm { font-size: 27px; line-height: 1.55; }
  .body-copy--xs { font-size: 23px; line-height: 1.5; }
  .body-copy p + p { margin-top: 1.4em; }

  .artwork {
    position: absolute;
    inset: 29px;
    background: linear-gradient(180deg, var(--green) 0%, var(--green) 70%, #8bbb2f 100%);
  }

  .response-page { padding: 0; display: block; }
  .response-page .steps {
    position: absolute;
    left: 29px; right: 29px; top: 29px;
    height: 360px;
    display: flex;
    align-items: center;
    justify-content: center;
    text-align: center;
    padding: 0 30px;
  }
  .response-page .prayer-band {
    position: absolute;
    left: 29px; right: 29px; bottom: 29px;
    height: 171px;
    background: var(--orange);
    display: flex;
    align-items: center;
    padding: 0 26px;
    font-size: 29px;
    line-height: 1.5;
    font-weight: 500;
  }
</style>
</head>
<body>
<main class="booklet">

  <section class="page page--green title-page">
    <h1 class="cover-title">Sun<br>On<br>Water</h1>
  </section>
  <section class="page page--green">
    <div class="artwork" role="img" aria-label="Three white crosses on a hill with tufts of grass"></div>
  </section>

  <section class="page page--sky title-page">
    <h2 class="section-title">God</h2>
  </section>
  <section class="page page--sky text-page">
    <div class="body-copy body-copy--lg">
      God is holy, that means He’s perfect.<br>In fact, He is so perfect,<br>corruption cannot live<br>with Him.
    </div>
  </section>

  <section class="page page--red title-page">
    <h2 class="section-title">Man</h2>
  </section>
  <section class="page page--red text-page">
    <div class="body-copy body-copy--lg">
      On the other hand,<br>mankind is corrupt.<br>For example,<br>we are selfish,<br>we are prideful,<br>and we lie.
    </div>
  </section>

  <section class="page page--orange title-page">
    <h2 class="section-title section-title--small">Problem</h2>
  </section>
  <section class="page page--orange text-page">
    <div class="body-copy body-copy--sm">
      And there is our big problem:<br>If God is perfect and corruption<br>cannot live with him… and we are corrupt…<br>WE cannot live with God.<br>Our corruption has cut us off from God…<br>now…AND when we die<br>which means we must spend eternity<br>in a place called hell…
    </div>
  </section>

  <section class="page page--navy title-page">
    <h2 class="section-title section-title--small">Christ</h2>
  </section>
  <section class="page page--navy text-page">
    <div class="body-copy body-copy--md">
      <p>But that is not what God wants.</p>
      <p>God loves you so much he<br>gave up his only Son to save you.<br>Jesus Christ died on the cross<br>in our place to pay for our sin<br>and rose again on the 3rd day.</p>
    </div>
  </section>

  <section class="page page--steel title-page">
    <h2 class="section-title section-title--small">Response</h2>
  </section>
  <section class="page page--steel response-page">
    <div class="steps">
      <div class="body-copy body-copy--xs">
        So now if anyone:<br><br>1. Agrees with God they are corrupt.<br>2. Believes Jesus Christ will save them.<br>3. And accepts Him as their<br>personal Lord and Savior.<br>Jesus Christ will forgive their corruption,<br>reconcile them to God,<br>and come and live inside them.
      </div>
    </div>
    <div class="prayer-band">
      You can pray to Jesus Christ right now and ask him to save you using the above three steps as your prayer guide.
    </div>
  </section>

</main>
</body>
</html>
```